Coastal Bright Sweep Business Card

We are a cleaning and waste management company with the slogan "making waste to landfill a thing of the past". We would like a re-design of our current business card. On the front we want to continue to use our logo as the focus point. On the back, we want the whole thing re-done to be less busy. We want the staff member’s name, the job title, mobile number, email and website. We do not want the address on the card. We still want the green, black and blue colours used, but a new font for the information on the back. Please do not change the logo design at all. We are also thinking about using icons to replace the text ‘mobile, email, website’. The “events + commercial” banner needs to be incorporated somewhere and needs to read “events + commercial + waste”. Another important point for consideration is that we are very concerned about being environmentally sustainable and will be printing on recycled paper. All designs should be made to compliment this in regards to boldness and colouring. Please find attached our logo, our colour chart and an image of our current business card.

```html
<!DOCTYPE html>
<html lang="en">
<head>
<meta charset="utf-8">
<title>Coastal Bright Sweep – Business Card</title>
<link rel="stylesheet" href="https://fonts.googleapis.com/css2?family=Montserrat:wght@700;800&family=Open+Sans:wght@400&display=swap">
<style>
  :root {
    --stage: #2e2e2e;
    --paper: #ffffff;
    --leaf: #80c242;
    --navy: #103f73;
    --sky: #00aeef;
    --ink: #111111;
  }
  * { box-sizing: border-box; margin: 0; padding: 0; }
  html, body { width: 1200px; height: 1200px; overflow: hidden; }
  body { background: var(--stage); position: relative; font-family: "Montserrat", sans-serif; }

  .card { position: absolute; left: 266px; width: 706px; height: 403px; overflow: hidden; }

  /* Front */
  .card--front { top: 209px; background: var(--paper); }
  .front__spine { position: absolute; left: 0; top: 0; width: 28px; height: 100%; background: var(--navy); }
  .front__band { position: absolute; left: 190px; top: 90px; right: 0; height: 217px; background: var(--leaf); }
  .front__seal {
    position: absolute; left: 58px; top: 72px; width: 264px; height: 264px; border-radius: 50%;
    background: var(--paper); border: 3px solid var(--leaf);
    display: flex; align-items: center; justify-content: center; text-align: center;
  }
  .front__name { color: var(--navy); font-weight: 800; font-size: 34px; line-height: 1.05; text-transform: uppercase; }
  .front__slogan {
    position: absolute; left: 282px; top: 315px; color: var(--ink);
    font-weight: 700; font-size: 13.3px; letter-spacing: 0.2px; text-transform: uppercase;
  }

  /* Back */
  .card--back { top: 630px; background: var(--leaf); }
  .back__seal {
    position: absolute; left: 80px; top: 25px; width: 156px; height: 156px; border-radius: 50%;
    background: var(--sky); display: flex; align-items: center; justify-content: center; text-align: center;
  }
  .back__brand { color: #fff; font-weight: 800; font-size: 21px; line-height: 1.05; text-transform: uppercase; }
  .staff { position: absolute; right: 55px; top: 88px; text-align: right; }
  .staff__name { font-weight: 800; font-size: 32px; letter-spacing: -0.5px; line-height: 1; color: var(--navy); }
  .staff__name span { color: var(--sky); }
  .staff__role { margin-top: 4px; font-weight: 700; font-size: 15px; letter-spacing: 1px; color: #fff; }
  .services {
    position: absolute; left: 131px; top: 198px; width: 443px; height: 36px; border-radius: 8px;
    background: var(--navy); color: var(--sky); font-weight: 700; font-size: 21px;
    display: flex; align-items: center; justify-content: center; letter-spacing: -0.3px;
  }
  .contact { position: absolute; right: 62px; top: 300px; list-style: none; font-family: "Open Sans", sans-serif; }
  .contact li {
    display: flex; align-items: center; justify-content: flex-end; gap: 12px;
    height: 25.5px; color: #fff; font-size: 15px; letter-spacing: 1px;
  }
  .contact svg { width: 16px; height: 16px; fill: var(--navy); flex: none; }
</style>
</head>
<body>
  <section class="card card--front" aria-label="Card front">
    <div class="front__spine"></div>
    <div class="front__band"></div>
    <div class="front__seal"><p class="front__name">Coastal<br>Bright<br>Sweep</p></div>
    <p class="front__slogan">Making waste to landfill a thing of the past</p>
  </section>

  <section class="card card--back" aria-label="Card back">
    <div class="back__seal"><p class="back__brand">Coastal<br>Bright<br>Sweep</p></div>
    <div class="staff">
      <p class="staff__name">JORDAN <span>MELLICK</span></p>
      <p class="staff__role">CLIENT MANAGER</p>
    </div>
    <p class="services">EVENTS + COMMERCIAL + WASTE</p>
    <ul class="contact">
      <li>0400-555-218
        <svg viewBox="0 0 24 24" aria-hidden="true"><path d="M6.6 10.8a15.1 15.1 0 0 0 6.6 6.6l2.2-2.2a1 1 0 0 1 1-.25 11.4 11.4 0 0 0 3.6.57 1 1 0 0 1 1 1V20a1 1 0 0 1-1 1A17 17 0 0 1 3 4a1 1 0 0 1 1-1h3.5a1 1 0 0 1 1 1c0 1.25.2 2.45.57 3.57a1 1 0 0 1-.25 1z"/></svg>
      </li>
      <li>jmellick@coastalbrightsweep.com.au
        <svg viewBox="0 0 24 24" aria-hidden="true"><path d="M2 5h20v14H2z M2 5l10 8 10-8" fill="none" stroke="#103f73" stroke-width="0"/><path d="M2 6.5V19h20V6.5l-10 7.5z"/><path d="M2 5h20l-10 7.3z"/></svg>
      </li>
      <li>www.coastalbrightsweep.com.au
        <svg viewBox="0 0 24 24" aria-hidden="true"><circle cx="12" cy="12" r="10"/><path d="M8 7c2 0 3 1 2.5 3S8 11 9 13s-1 3 0 5M15 5c-1 2 1 3 3 3M14 14c1-1 3 0 3 2s-1 3-2 3" fill="none" stroke="#80c242" stroke-width="1.6" stroke-linecap="round"/></svg>
      </li>
    </ul>
  </section>
</body>
</html>
```